Analytics software company needs a business card design

We need a business card design for a global analytics software provider called 'Varnel Software'. Our main focus is developing real estate analysis software. We are open to any color scheme. The final design should be simple, modern, and precise.
Updates

There is one day left in our project and we are still looking forward to receiving additional submissions. We look forward to selecting one of your designs. Thanks.

Industry/Entity Type

Real Estate

```html
<!DOCTYPE html>
<html lang="en">
<head>
<meta charset="utf-8">
<title>Varnel Software — Business Card</title>
<link rel="stylesheet" href="https://fonts.googleapis.com/css2?family=Michroma&display=swap">
<style>
  :root {
    --backdrop: #e4e4e4;
    --card: #ffffff;
    --ink: #4a4a4a;
    --brand-blue: #1f4e9c;
    --band-blue: #2a73d0;
    --band-deep: #2a47a8;
    --brand-green: #4caf2a;
    --rule: #b9b9b9;
  }
  * { margin: 0; padding: 0; box-sizing: border-box; }
  html, body {
    width: 1200px; height: 900px; overflow: hidden;
    background: radial-gradient(circle at 50% 40%, #f4f4f4, var(--backdrop));
    font-family: "Michroma", sans-serif;
    color: var(--ink);
  }
  .card {
    position: absolute; left: 120px; top: 170px;
    width: 960px; height: 560px;
    background: var(--card);
    box-shadow: 0 18px 40px rgba(0,0,0,0.18);
    overflow: hidden;
  }
  .brand {
    position: absolute; left: 150px; top: 140px;
    display: flex; align-items: center; gap: 18px;
  }
  .brand-dot {
    width: 64px; height: 64px; border-radius: 50%;
    background: var(--brand-blue);
  }
  .brand-name {
    font-size: 34px; color: var(--brand-blue);
    letter-spacing: 1px; line-height: 1.1;
  }
  .identity {
    position: absolute; left: 232px; top: 250px;
    text-align: right; width: 230px;
  }
  .person-name { font-size: 17px; color: #333; letter-spacing: 1px; }
  .person-role { font-size: 12px; margin-top: 6px; letter-spacing: 1px; }
  .address {
    position: absolute; left: 150px; top: 330px; width: 312px;
    text-align: right; font-size: 13px; line-height: 1.6; letter-spacing: 1px;
  }
  .divider {
    position: absolute; left: 492px; top: 230px;
    width: 1px; height: 130px; background: var(--rule);
  }
  .contacts {
    position: absolute; left: 514px; top: 226px;
    list-style: none; font-size: 13px; letter-spacing: 1px;
  }
  .contacts li { display: flex; align-items: center; gap: 10px; height: 24px; }
  .contacts li.gap { margin-top: 10px; }
  .contacts svg { width: 14px; height: 14px; flex: none; }
  .band { position: absolute; left: 0; bottom: 0; width: 960px; height: 200px; }
  .band-url { font-size: 15px; fill: #ffffff; letter-spacing: 3px; }
</style>
</head>
<body>
  <main class="card">
    <div class="brand">
      <div class="brand-dot"></div>
      <div class="brand-name">VARNEL<br>SOFTWARE</div>
    </div>

    <div class="identity">
      <p class="person-name">ELENA MARSH</p>
      <p class="person-role">OWNER / C.E.O</p>
    </div>

    <p class="address">SUITE # 410, KELL BLDG,<br>NY 10482</p>

    <div class="divider"></div>

    <ul class="contacts">
      <li>
        <svg viewBox="0 0 14 14"><circle cx="7" cy="7" r="7" fill="#444"/><path d="M4.5 3.5l1.5 0 .6 2-1 .8a5 5 0 0 0 2.1 2.1l.8-1 2 .6 0 1.5c-3.5.3-6.3-2.5-6-6z" fill="#fff"/></svg>
        212-555-0148
      </li>
      <li>
        <svg viewBox="0 0 14 14"><circle cx="7" cy="7" r="7" fill="#444"/><rect x="4.5" y="3" width="5" height="8" rx="1" fill="#fff"/></svg>
        212-555-0173
      </li>
      <li>
        <svg viewBox="0 0 14 14"><circle cx="7" cy="7" r="7" fill="#444"/><rect x="3.5" y="5" width="7" height="5" fill="#fff"/><rect x="5" y="3" width="4" height="2" fill="#fff"/></svg>
        212-555-0196
      </li>
      <li class="gap">
        <svg viewBox="0 0 14 14"><circle cx="7" cy="7" r="7" fill="#444"/><rect x="3.5" y="4.5" width="7" height="5" fill="#fff"/><path d="M3.5 4.5L7 7.5l3.5-3" stroke="#444" stroke-width="0.8" fill="none"/></svg>
        ELENA@VARNELSOFTWARE.COM
      </li>
      <li>
        <svg viewBox="0 0 14 14"><circle cx="7" cy="7" r="7" fill="#444"/><circle cx="7" cy="7" r="4" fill="none" stroke="#fff" stroke-width="0.9"/><path d="M3 7h8M7 3v8" stroke="#fff" stroke-width="0.9"/></svg>
        WWW.VARNELSOFTWARE.COM
      </li>
    </ul>

    <svg class="band" viewBox="0 0 960 200" aria-hidden="true">
      <defs>
        <linearGradient id="band-fill" x1="0" y1="0" x2="1" y2="0">
          <stop offset="0" stop-color="var(--band-deep)"/>
          <stop offset="0.6" stop-color="var(--band-blue)"/>
          <stop offset="1" stop-color="var(--band-deep)"/>
        </linearGradient>
        <path id="url-path" d="M200,176 Q520,128 900,150"/>
      </defs>
      <path d="M0,200 Q460,80 960,110" fill="none" stroke="var(--brand-green)" stroke-width="6"/>
      <path d="M0,200 Q460,92 960,122 L960,200 Z" fill="url(#band-fill)"/>
      <text class="band-url"><textPath href="#url-path" startOffset="50%" text-anchor="middle">WWW.VARNELSOFTWARE.COM</textPath></text>
    </svg>
  </main>
</body>
</html>
```